Hispanic Financial Counseling and Advocate Firm seeks business card design

Looking for a clean, professional business card design. This is a firm that specializes in providing financial education, coaching, and planning to the Hispanic community. The name of the company is Valemar, which means to prosper. We need a design that is clean, professional, and invokes trust, professionalism, but also welcoming. Our logo is a plant growing from a hand to give the messaging of of being in control of growing your financial future and security. Its part of a larger organization names Celesta Financial Group, who's logo is a tree with multi colored branches. We have the back of the card designed so we just need the front designed. the back is blue, so front needs to be a different background color, not blue.

Target Market(s)

Hispanic Community looking to better their future

Industry/Entity Type

financial services

Contact Information for Business Card

contact info: Anselmo Ibarra Jr, 951-555-0147, info@celestafinancialgroup.example. Celestafinancialgroup.example. tag line: Para un futuro mas seguro!

Requirements
Must have
• basics: logo, contact info.
Nice to have
• possibly incorporate the tree logo provided somehow
Should not have
• should not look like the back, needs to be different from the back provided.

```html
<!DOCTYPE html>
<html lang="es">
<head>
<meta charset="utf-8">
<title>Valemar – Business Card Front</title>
<link rel="stylesheet" href="https://fonts.googleapis.com/css2?family=Montserrat:wght@400;600;700&display=swap">
<style>
  :root {
    --stage: #3f4746;
    --card: #ffffff;
    --green: #6aa542;
    --navy: #4a5572;
    --text: #4a5572;
    --emblem-soft: #e4f0da;
  }
  html, body {
    margin: 0;
    width: 1200px;
    height: 780px;
    overflow: hidden;
    background: var(--stage);
    font-family: "Montserrat", sans-serif;
  }
  .canvas {
    position: relative;
    width: 1200px;
    height: 780px;
  }
  .card {
    position: absolute;
    left: 75px;
    top: 90px;
    width: 1050px;
    height: 600px;
    background: var(--card);
    overflow: hidden;
    box-shadow: 0 14px 30px rgba(0,0,0,.35);
  }
  .card-art {
    position: absolute;
    inset: 0;
    width: 1050px;
    height: 600px;
  }
  .brand {
    position: absolute;
    left: 80px;
    top: 82px;
    display: flex;
    align-items: center;
    gap: 12px;
  }
  .brand-dot {
    width: 22px;
    height: 22px;
    border-radius: 50%;
    background: var(--green);
  }
  .brand-name {
    font-weight: 700;
    font-size: 38px;
    color: var(--green);
    letter-spacing: .5px;
  }
  .holder {
    position: absolute;
    left: 150px;
    top: 210px;
  }
  .holder-name {
    margin: 0;
    font-weight: 700;
    font-size: 44px;
    color: var(--navy);
    letter-spacing: .5px;
  }
  .holder-rule {
    width: 64px;
    height: 5px;
    background: var(--green);
    margin-top: 6px;
  }
  .contact-list {
    list-style: none;
    margin: 22px 0 0 28px;
    padding: 0;
  }
  .contact-item {
    display: flex;
    align-items: center;
    gap: 14px;
    font-size: 20px;
    color: var(--text);
    margin-bottom: 12px;
  }
  .contact-icon {
    width: 26px;
    height: 26px;
    flex: none;
  }
</style>
</head>
<body>
<main class="canvas">
  <section class="card" aria-label="Valemar business card front">
    <svg class="card-art" viewBox="0 0 1050 600" aria-hidden="false">
      <defs>
        <radialGradient id="emblem-fill" cx="50%" cy="50%" r="50%">
          <stop offset="0%" stop-color="var(--emblem-soft)"/>
          <stop offset="100%" stop-color="#ffffff" stop-opacity="0"/>
        </radialGradient>
        <path id="tagline-path" d="M330 585 C520 478 720 438 990 372"/>
      </defs>
      <rect class="emblem-area" x="560" y="20" width="470" height="400" fill="url(#emblem-fill)" role="img" aria-label="Large brand emblem area: a plant growing from an open hand"/>
      <path class="band-gap" d="M250 600 C470 460 700 405 1050 312 L1050 600 Z" fill="#ffffff"/>
      <path class="band" d="M270 600 C480 470 700 420 1050 330 L1050 600 Z" fill="var(--green)"/>
      <text class="tagline" font-family="Montserrat, sans-serif" font-weight="600" font-size="22" letter-spacing="7" fill="#ffffff">
        <textPath href="#tagline-path">Para un futuro mas seguro!</textPath>
      </text>
    </svg>

    <div class="brand">
      <span class="brand-dot"></span>
      <span class="brand-name">Valemar</span>
    </div>

    <div class="holder">
      <h1 class="holder-name">Anselmo Ibarra Jr</h1>
      <div class="holder-rule"></div>
      <ul class="contact-list">
        <li class="contact-item">
          <svg class="contact-icon" viewBox="0 0 26 26"><circle cx="13" cy="13" r="13" fill="var(--green)"/><path d="M9 7.5c1-.6 1.8 1.6 2.2 2.4.3.7-.9 1.3-.7 1.9.5 1.4 1.9 2.8 3.3 3.3.6.2 1.2-1 1.9-.7.8.4 3 1.2 2.4 2.2-.7 1.1-2 1.6-3.2 1.2-3-1-5.5-3.5-6.5-6.5-.4-1.2.1-2.5 1.2-3.2z" fill="#fff"/></svg>
          <span>951-555-0147</span>
        </li>
        <li class="contact-item">
          <svg class="contact-icon" viewBox="0 0 26 26"><circle cx="13" cy="13" r="13" fill="var(--green)"/><rect x="7" y="8.5" width="12" height="9" rx="1" fill="#fff"/><path d="M7.5 9l5.5 4.5 5.5-4.5" fill="none" stroke="var(--green)" stroke-width="1.3"/></svg>
          <span>info@celestafinancialgroup.example</span>
        </li>
        <li class="contact-item">
          <svg class="contact-icon" viewBox="0 0 26 26"><circle cx="13" cy="13" r="13" fill="var(--green)"/><g fill="none" stroke="#fff" stroke-width="1.3"><circle cx="13" cy="13" r="6"/><ellipse cx="13" cy="13" rx="2.6" ry="6"/><path d="M7 13h12"/></g></svg>
          <span>www.Celestafinancialgroup.example</span>
        </li>
      </ul>
    </div>
  </section>
</main>
</body>
</html>
```